Computer consultant business card

Brimlo Software is a newly started computer consulting company. It's a small one-man company that provides mostly Velunix applications but also websites in collaboration with designers. I'm running this company on the side of full time university studies.

I want the final design to be clean and memorable. Be creative! :)

Some inspiration:
http://www.tavelpix.net/design/73519
http://www.tavelpix.net/design/2739566/business-card-design-by-quillbop
http://www.tavelpix.net/design/804613/business-card-design-by-lorvena-brukwaldsen

See attachment for my company logo.
Updates

I would like to thank everyone for submitting! I'll need a couple of days to review and ultimately select a design.

Target Market(s)

Non-technical entrepreneurs and small companies.

Industry/Entity Type

University

Requirements
Must have
• My company logo.
In any way, both colors from my logo.
First- and last name, e-mail and phone number.
Double-sided design.
Nice to have
• Something creative with the symbol in my logo

```html
<!DOCTYPE html>
<html lang="en">
<head>
<meta charset="utf-8">
<title>Brimlo Software – Business Card</title>
<link rel="stylesheet" href="https://fonts.googleapis.com/css2?family=Arimo:wght@400&display=swap">
<style>
  :root {
    --backdrop: #d4d4d4;
    --card-black: #000000;
    --band-grey: #2b2b2b;
    --brand-grey: #353233;
    --brand-blue: #4472bd;
    --text-white: #ffffff;
    --shadow: rgba(0, 0, 0, 0.35);
  }
  * { margin: 0; padding: 0; box-sizing: border-box; }
  html, body {
    width: 1200px;
    height: 900px;
    overflow: hidden;
    background: var(--backdrop);
    font-family: "Arimo", Arial, sans-serif;
  }
  .canvas { position: relative; width: 1200px; height: 900px; }

  .card {
    position: absolute;
    width: 614px;
    height: 338px;
    border-radius: 18px;
    overflow: hidden;
    background: var(--card-black);
    box-shadow: 0 4px 12px var(--shadow);
  }
  .card--front { left: 104px; top: 72px; }
  .card--back  { left: 484px; top: 482px; }

  .band {
    position: absolute;
    left: 0;
    width: 100%;
    background: var(--band-grey);
  }
  .band--top { top: 0; height: 68px; }
  .band--bottom { bottom: 0; height: 68px; }

  /* Front: name with a plain dot */
  .brand {
    position: absolute;
    display: flex;
    align-items: center;
    gap: 10px;
  }
  .brand__dot {
    border-radius: 50%;
    background: var(--brand-blue);
    flex: none;
  }
  .brand__name {
    color: var(--brand-grey);
    font-weight: 400;
    line-height: 1;
  }
  .card--front .brand { left: 88px; top: 138px; }
  .card--front .brand__dot { width: 34px; height: 34px; }
  .card--front .brand__name { font-size: 48px; color: #5a5758; }

  .contact {
    position: absolute;
    left: 323px;
    top: 129px;
    list-style: none;
    color: var(--text-white);
    font-size: 18px;
    line-height: 30.5px;
  }

  /* Back: large plain disc with the name in the corner */
  .back-disc {
    position: absolute;
    left: 8px;
    top: 10px;
    width: 318px;
    height: 318px;
    border-radius: 50%;
    background: var(--brand-blue);
  }
  .web {
    position: absolute;
    right: 87px;
    top: 233px;
    color: var(--text-white);
    font-size: 16px;
    line-height: 1;
  }
  .back-name {
    position: absolute;
    right: 10px;
    bottom: 20px;
    color: var(--brand-grey);
    font-size: 68px;
    line-height: 1;
  }
</style>
</head>
<body>
<main class="canvas">
  <section class="card card--front" aria-label="Business card front">
    <div class="band band--top"></div>
    <div class="band band--bottom"></div>
    <div class="brand">
      <span class="brand__dot"></span>
      <span class="brand__name">brimlo</span>
    </div>
    <ul class="contact">
      <li>First- and last name</li>
      <li>e-mail</li>
      <li>phone number</li>
    </ul>
  </section>

  <section class="card card--back" aria-label="Business card back">
    <div class="back-disc"></div>
    <p class="web">www.brimlo.net</p>
    <p class="back-name">brimlo</p>
  </section>
</main>
</body>
</html>
```